Brochure for medical doctor

I need a brochure for a medical doctor to promote his practice. The brochure should contain his picture, business information (use letterhead from attachment), and the following text:

- Now accepting PI cases on lien!
- Same and next business day appointments available for initial visits, pre-operative clearances, and all other medical needs

- Expedited medical reports sent quickly to your office

Medical

```html
<!DOCTYPE html>
<html lang="en">
<head>
<meta charset="utf-8">
<title>Meadowbrook Medical Center Brochure</title>
<link href="https://fonts.googleapis.com/css2?family=Oswald:wght@400;500;600&family=Roboto+Condensed:wght@300;400&family=Montserrat:wght@400;700&display=swap" rel="stylesheet">
<style>
:root{
  --red:#c8161d;
  --red-dark:#a90f15;
  --ink:#1e1e1e;
  --body:#4a4a4a;
  --paper:#ffffff;
  --fold:#e4e4e4;
  --backdrop:#b3b3b3;
}
*{margin:0;padding:0;box-sizing:border-box}
html,body{width:959px;height:1200px;overflow:hidden;background:var(--backdrop)}
.stage{position:absolute;left:0;top:0;width:1592px;height:1992px;transform:scale(.60240);transform-origin:0 0;font-family:"Montserrat",sans-serif}
.abs{position:absolute}
.sheet{position:absolute;left:233px;width:1112px;height:786px;background:var(--paper);box-shadow:0 3px 6px rgba(0,0,0,.25);overflow:hidden}
.sheet-outer{top:169px}
.sheet-inner{top:1038px}
.panel{position:absolute;top:0;height:100%}
.panel-shaded{background:linear-gradient(90deg,#ffffff 0%,#f4f4f4 70%,#e6e6e6 100%)}
.panel-center{background:linear-gradient(90deg,#dcdcdc 0%,#f2f2f2 30%,#f0f0f0 80%,#dcdcdc 100%)}
.section-title{position:absolute;background:var(--red);color:#fff;font-family:"Oswald",sans-serif;font-weight:500;font-size:25px;display:flex;align-items:center;justify-content:center;gap:10px}
.section-title .mark{width:20px;height:20px;background:#fff}
.service-bar{position:absolute;background:var(--red);color:#fff;font-weight:700;font-size:16px;display:flex;align-items:center;padding-left:14px;white-space:nowrap;overflow:hidden}
.service-bar.long{font-size:14.6px;letter-spacing:-.2px}
.copy{position:absolute;font-size:10.4px;line-height:13.6px;letter-spacing:-.3px;color:var(--body);text-align:justify;hyphens:auto;-webkit-hyphens:auto}
.copy p+p{margin-top:13px}
.photo{position:absolute}
.feature-box{position:absolute;left:22px;top:588px;width:318px;height:172px;background:var(--red);clip-path:polygon(0 0,285px 0,318px 30px,318px 172px,0 172px)}
.feature{position:absolute;left:70px;color:#fff;font-weight:700;font-size:13.6px;line-height:17.5px;letter-spacing:-.1px;white-space:nowrap}
.feature-icon{position:absolute;left:22px}
.contact-block{position:absolute;left:371px;top:416px;width:341px;height:369px;background:var(--ink);color:#fff;font-family:"Roboto Condensed",sans-serif;font-weight:300}
.contact-line{position:absolute;left:41px;white-space:nowrap}
.rule{position:absolute;left:39px;width:257px;height:1px;background:#777}
.brand{position:absolute;display:flex;align-items:center;gap:10px}
.brand .square{width:26px;height:26px;background:var(--red)}
.brand .name{font-family:"Oswald",sans-serif;font-weight:600;color:#2b2b2b;font-size:24px;line-height:26px;letter-spacing:.2px;white-space:nowrap}
.headline{position:absolute;left:0;width:373px;text-align:center;font-family:"Oswald",sans-serif;font-weight:500;font-size:52px;line-height:54px;letter-spacing:-1px;white-space:nowrap;transform:scaleX(.8);transform-origin:50% 0}
.url-tag{position:absolute;left:48px;width:268px;text-align:center;font-family:"Roboto Condensed",sans-serif;color:var(--red);font-size:17px;border-top:1px solid #f1c7c9;border-bottom:1px solid #f1c7c9;padding:7px 0;white-space:nowrap}
.phone-big{position:absolute;font-family:"Oswald",sans-serif;font-weight:500;color:var(--red);font-size:50px;line-height:56px;white-space:nowrap}
.url-big{position:absolute;font-family:"Roboto Condensed",sans-serif;font-weight:400;color:#1e1e1e;font-size:19px;letter-spacing:.4px;white-space:nowrap}
</style>
</head>
<body>
<div class="stage">

  <section class="sheet sheet-outer">
    <div class="panel panel-shaded" style="left:0;width:371px">
      <div class="section-title" style="left:27px;top:24px;width:313px;height:44px"><span class="mark"></span>ABOUT US</div>
      <div class="photo" role="img" aria-label="Smiling nurse in blue scrubs with a caregiver helping an older man with a walker" style="left:27px;top:75px;width:313px;height:212px;background:linear-gradient(100deg,#e9eef2 0%,#b8c7d9 45%,#dfe7ea 70%,#9fb3cf 100%)"></div>
      <div class="copy" style="left:27px;top:297px;width:313px">
        <p>With a commitment to providing comprehensive, compassionate care, Daniel Marlow, MD provides a wide range of top-notch health services to patients from in and around Fairhaven, California. He is the driving force behind Meadowbrook Medical Center, a renowned clinic that serves the men, women, and children of the greater Fairhaven community.</p>
        <p>Dr. Marlow began his medical education as an undergraduate at Westbrook State University, where he developed a passion for medicine. He graduated from Westbrook State summa cum laude, and went on to medical school at Harbor Point School of Medicine.</p>
        <p>Dr. Marlow completed his residency at Valley Crest Medical Center in Ridgefield, California, and was among the top students in his graduating class. In 2008, he went into private practice in Fairhaven.</p>
      </div>
      <div class="feature-box">
        <svg class="feature-icon" style="top:28px" width="28" height="28" viewBox="0 0 28 28" fill="none" stroke="#fff" stroke-width="1.6"><rect x="2" y="4" width="24" height="21" rx="1"/><line x1="2" y1="10" x2="26" y2="10"/><line x1="8" y1="1" x2="8" y2="6"/><line x1="20" y1="1" x2="20" y2="6"/><rect x="6" y="13" width="4" height="3"/><rect x="12" y="13" width="4" height="3"/><rect x="18" y="13" width="4" height="3"/><rect x="12" y="19" width="4" height="3"/><rect x="18" y="19" width="4" height="3"/></svg>
        <div class="feature" style="top:23px">Same &amp; next business day<br>appointments available for initial<br>visits, pre-operative clearances,<br>&amp; all other medical needs</div>
        <svg class="feature-icon" style="top:110px;left:14px" width="42" height="36" viewBox="0 0 42 36" fill="none" stroke="#fff" stroke-width="1.8"><circle cx="25" cy="18" r="14"/><polyline points="25,10 25,18 31,21"/><line x1="2" y1="13" x2="10" y2="13"/><line x1="0" y1="19" x2="9" y2="19"/><line x1="3" y1="25" x2="11" y2="25"/></svg>
        <div class="feature" style="top:111px">Expedited medical reports<br>sent quickly to your office</div>
      </div>
    </div>

    <div class="photo" role="img" aria-label="Red-tinted close-up of a doctor holding a stethoscope with floating medical icons" style="left:371px;top:0;width:341px;height:369px;background:linear-gradient(135deg,#d7262c 0%,#b51419 55%,#8a0d11 100%)"></div>
    <div class="abs" style="left:712px;top:0;width:27px;height:786px;background:var(--fold)"></div>
    <div class="contact-block">
      <div class="contact-line" style="top:76px;font-size:21px">MEADOWBROOK MEDICAL CENTER</div>
      <div class="contact-line" style="top:98px;font-size:33px">4510 LINDEN AVE</div>
      <div class="contact-line" style="top:136px;font-size:24px">FAIRHAVEN, CA, 90000</div>
      <div class="contact-line" style="top:175px;font-size:36px">TEL (555) 214-3300</div>
      <div class="contact-line" style="top:214px;font-size:36px">FAX (555) 214-3301</div>
      <div class="rule" style="top:274px"></div>
      <div class="contact-line" style="top:283px;font-size:16.5px;font-weight:400;letter-spacing:.4px">WWW.MEADOWBROOKMEDICAL.COM</div>
      <div class="rule" style="top:311px"></div>
    </div>
    <svg class="abs" style="left:640px;top:298px" width="200" height="200" viewBox="0 0 200 200" role="img" aria-label="Nurse walking with an elderly woman outdoors">
      <polygon points="100,6 194,100 100,194 6,100" fill="#fff"/>
      <polygon points="101,8 189,96 101,184 13,96" fill="#8fa6b8"/>
    </svg>

    <div class="panel" style="left:739px;width:373px">
      <div class="brand" style="left:50px;top:68px"><span class="square"></span><span class="name">MEADOWBROOK MEDICAL<br>CENTER</span></div>
      <div class="headline" style="top:142px;color:var(--red)">NOW ACCEPTING</div>
      <div class="headline" style="top:192px;color:#151515">PI CASES ON LIEN!</div>
      <div class="url-tag" style="top:262px">WWW.MEADOWBROOKMEDICAL.COM</div>
      <div class="photo" role="img" aria-label="Hands of a clinician in blue scrubs holding a stethoscope" style="left:33px;top:416px;width:340px;height:370px;background:linear-gradient(160deg,#a9cde0 0%,#6aa4c6 50%,#c9ad9b 100%)"></div>
    </div>
  </section>

  <section class="sheet sheet-inner">
    <div class="panel" style="left:0;width:373px">
      <div class="section-title" style="left:27px;top:30px;width:313px;height:43px"><span class="mark"></span>SERVICES</div>
      <div class="photo" role="img" aria-label="Two smiling doctors holding a red heart" style="left:27px;top:83px;width:312px;height:216px;background:linear-gradient(110deg,#dfe5ea 0%,#f3f4f5 40%,#e7d6c6 70%,#dfe5ea 100%)"></div>
      <div class="service-bar" style="left:27px;top:307px;width:311px;height:32px">STD Testing</div>
      <div class="copy" style="left:26px;top:347px;width:313px">Is HIV still a serious health risk ?<br>Statistics suggest that the rate of HIV transmission is down and fewer people are contracting the disease. That decline is attributed to improvements in drug therapies that suppress the virus in affected people who are receiving treatment and new prevention methods.</div>
      <div class="service-bar" style="left:27px;top:446px;width:310px;height:32px">Cold &amp; Flu</div>
      <div class="copy" style="left:26px;top:492px;width:313px">What is the difference between a cold and the flu ?<br>A cold is a mild respiratory illness that can present symptoms that last for several days. While a cold is never a pleasant experience, its discomfort is far less than what you experience with the flu.</div>
      <div class="photo" role="img" aria-label="Woman in bed under a blanket blowing her nose" style="left:27px;top:572px;width:314px;height:181px;background:linear-gradient(120deg,#f1ece6 0%,#d9cbbd 50%,#6b5446 100%)"></div>
    </div>

    <div class="panel panel-center" style="left:373px;width:366px">
      <div class="service-bar" style="left:28px;top:30px;width:311px;height:33px">I - 693</div>
      <div class="copy" style="left:27px;top:70px;width:312px">an I have my family doctor perform my I-693 exam ?<br>To ensure strict examination standards are followed, only approved civil surgeons are allowed to administer the I-693 exam. Unless your family physician is authorized to provide this service, a qualified surgeon needs to complete your exam.</div>
      <div class="service-bar" style="left:27px;top:168px;width:311px;height:33px">Obstetrician</div>
      <div class="photo" role="img" aria-label="Nurse feeding an elderly woman a meal in a care room" style="left:27px;top:212px;width:310px;height:246px;background:linear-gradient(120deg,#9bc3d6 0%,#cfdde6 50%,#d98a4a 100%)"></div>
      <div class="copy" style="left:25px;top:467px;width:313px">Is HIV still a serious health risk ?<br>Statistics suggest that the rate of HIV transmission is down and fewer people are contracting the disease. That decline is attributed to improvements in drug therapies that suppress the virus in affected people who are receiving treatment and new prevention methods.</div>
      <div class="service-bar" style="left:24px;top:569px;width:310px;height:33px">Prostate Cancer Screenings</div>
      <div class="copy" style="left:22px;top:612px;width:313px">What is prostate cancer ?<br>Your prostate is a small gland that is approximately the same size and shape as a walnut. It sits in front of your rectum and below your bladder.</div>
      <div class="brand" style="left:30px;top:694px"><span class="square"></span><span class="name">MEADOWBROOK MEDICAL<br>CENTER</span></div>
    </div>

    <div class="panel" style="left:739px;width:373px">
      <div class="service-bar" style="left:33px;top:34px;width:310px;height:32px">First Aid Care</div>
      <div class="copy" style="left:31px;top:74px;width:312px">Is HIV still a serious health risk ?<br>Statistics suggest that the rate of HIV transmission is down and fewer people are contracting the disease. That decline is attributed to improvements in drug therapies that suppress the virus in affected people who are receiving treatment and new prevention methods.</div>
      <div class="service-bar long" style="left:33px;top:171px;width:310px;height:32px">Well Child Exams &amp; Immunizations</div>
      <div class="copy" style="left:31px;top:212px;width:312px">What is the difference between a cold and the flu ?<br>A cold is a mild respiratory illness that can present symptoms that last for several days. While a cold is never a pleasant experience, its discomfort is far less than what you experience with the flu.</div>
      <div class="service-bar" style="left:33px;top:296px;width:310px;height:32px">Well Women Care</div>
      <div class="copy" style="left:31px;top:339px;width:312px">an I have my family doctor perform my I-693 exam ?<br>To ensure strict examination standards are followed, only approved civil surgeons are allowed to administer the I-693 exam. Unless your family physician is authorized to provide this service, a qualified surgeon needs to complete your exam.</div>
      <div class="photo" role="img" aria-label="Smiling woman relaxing on a couch holding a mug" style="left:33px;top:440px;width:309px;height:202px;background:linear-gradient(120deg,#8fd3cf 0%,#b9e4e0 45%,#8a6a55 75%,#e06a2a 100%)"></div>
      <div class="phone-big" style="left:33px;top:676px">(555) 214-3300</div>
      <div class="url-big" style="left:35px;top:736px">WWW.MEADOWBROOKMEDICAL.COM</div>
    </div>
  </section>

</div>
</body>
</html>
```